Website Design for Vexilum

Vexilum is a website and app that sends notifications to users about entertainment events that they are interested in (sport, music, festivals, comedy, art etc.). Users will also post videos, photos and other comments about the event. It targets generatio

```html
<!DOCTYPE html>
<html lang="en">
<head>
<meta charset="utf-8">
<title>Vexilum – Personalised Events Guide</title>
<link rel="stylesheet" href="https://fonts.googleapis.com/css2?family=Lato:wght@400;700&display=swap">
<style>
  :root {
    --page-bg: #f1f1f0;
    --ink: #2b3440;
    --muted: #5a5f66;
    --band-blue: #1a55a3;
    --band-blue-dark: #144789;
    --button-top: #3a7fc6;
    --button-bottom: #1c5596;
    --button-edge: #174a82;
    --link-orange: #d9782c;
    --frame: #2c3b4d;
    --logo-ink: #2f3338;
    --logo-dot: #e8b920;
    --rule: #8a8f94;
  }
  * { box-sizing: border-box; margin: 0; padding: 0; }
  html, body { width: 1200px; height: 780px; overflow: hidden; }
  body {
    position: relative;
    background: var(--page-bg);
    font-family: "Lato", sans-serif;
    color: var(--ink);
  }
  .site-header { position: absolute; left: 0; top: 0; width: 1200px; height: 89px; }
  .brand {
    position: absolute; left: 190px; top: 24px;
    display: flex; align-items: center; gap: 8px;
    font-size: 40px; font-weight: 700; color: var(--logo-ink);
    letter-spacing: -0.5px; line-height: 1;
  }
  .brand-dot { width: 30px; height: 30px; border-radius: 50%; background: var(--logo-dot); }
  .header-nav {
    position: absolute; left: 770px; top: 31px;
    display: flex; align-items: center; gap: 8px;
  }
  .greeting { font-size: 14px; color: var(--muted); margin-right: 14px; }
  .btn {
    display: inline-flex; align-items: center; justify-content: center;
    color: #fff; text-decoration: none;
    background: linear-gradient(var(--button-top), var(--button-bottom));
    border: 1px solid var(--button-edge); border-radius: 4px;
    box-shadow: 0 1px 2px rgba(0,0,0,.3);
  }
  .btn-nav { height: 29px; padding: 0 10px; font-size: 19px; }
  .hero-band {
    position: absolute; left: 0; top: 89px; width: 1200px; height: 278px;
    background: linear-gradient(var(--band-blue), var(--band-blue-dark));
  }
  .hero-shadow {
    position: absolute; left: 380px; top: 366px; width: 440px; height: 30px;
    border-radius: 50%;
    background: radial-gradient(ellipse at center, rgba(0,0,0,.45), rgba(0,0,0,0) 70%);
  }
  .hero-frame {
    position: absolute; left: 347px; top: 89px; width: 498px; height: 279px;
    background: var(--frame); padding: 8px 10px 10px;
    box-shadow: 0 0 30px rgba(0,0,0,.45);
  }
  .hero-photo {
    width: 100%; height: 100%;
    background: radial-gradient(ellipse at 50% 40%, #6b6a4f, #2d2c26 55%, #141518);
  }
  .slide-next {
    position: absolute; left: 555px; top: 203px; width: 56px; height: 56px;
    background: rgba(40,110,190,.85);
  }
  .tagline {
    position: absolute; left: 300px; top: 406px; width: 600px;
    text-align: center; font-size: 16px; font-weight: 700; line-height: 22px;
  }
  .cta-row { position: absolute; left: 364px; top: 479px; width: 461px; height: 42px; }
  .btn-cta { position: absolute; top: 0; height: 42px; width: 195px; font-size: 14px; }
  .btn-connect { left: 0; justify-content: flex-start; padding-left: 8px; gap: 14px; }
  .connect-mark { width: 16px; height: 22px; background: rgba(255,255,255,.85); border-radius: 2px; }
  .btn-find { left: 265px; font-size: 15px; }
  .cta-or {
    position: absolute; left: 195px; width: 70px; top: 10px;
    text-align: center; font-size: 18px; font-weight: 700; color: var(--muted);
  }
  .account-help {
    position: absolute; left: 300px; top: 572px; width: 600px;
    text-align: center; font-size: 14px; line-height: 23px; color: var(--muted);
  }
  a.text-link { color: var(--link-orange); }
  .footer-rule {
    position: absolute; left: 275px; top: 655px; width: 640px;
    border-top: 1px solid var(--rule);
  }
  .footer-col { position: absolute; top: 679px; font-size: 14px; line-height: 22px; }
  .footer-col h3 { font-size: 14px; font-weight: 700; color: var(--ink); margin-bottom: 1px; }
  .footer-col a { display: block; color: var(--link-orange); }
  .footer-col a.strong { font-weight: 700; }
  .col-legal { left: 353px; }
  .col-crew { left: 560px; }
  .col-business { left: 779px; }
</style>
</head>
<body>
  <header class="site-header">
    <div class="brand"><span class="brand-dot"></span>Vexilum</div>
    <nav class="header-nav">
      <span class="greeting">G'Day mate</span>
      <a class="btn btn-nav" href="#">Sign-up</a>
      <a class="btn btn-nav" href="#">Log-in</a>
    </nav>
  </header>

  <section class="hero-band"></section>
  <div class="hero-shadow"></div>
  <div class="hero-frame">
    <div class="hero-photo" role="img" aria-label="Photo of a packed crowd dancing with raised hands at a live night event"></div>
  </div>
  <svg class="slide-next" viewBox="0 0 56 56" aria-label="Next slide">
    <polyline points="23,17 34,28 23,39" fill="none" stroke="#fff" stroke-width="2.5"/>
  </svg>

  <p class="tagline">Vexilum is a personalised mobile and online events guide which prevents<br>social Aussies missing out on events they'd like to see</p>

  <div class="cta-row">
    <a class="btn btn-cta btn-connect" href="#"><span class="connect-mark"></span>Connect with Friendlink</a>
    <span class="cta-or">- OR -</span>
    <a class="btn btn-cta btn-find" href="#">Find Event</a>
  </div>

  <p class="account-help">Exiting users: <a class="text-link" href="#">Log in</a><br><a class="text-link" href="#">How does Vexilum work?</a></p>

  <div class="footer-rule"></div>
  <footer>
    <div class="footer-col col-legal">
      <h3>Legal Mumbo Jumbo</h3>
      <a href="#">Privacy Policy</a>
      <a href="#">Terms &amp; Conditions</a>
      <a href="#">Code of Conduct</a>
    </div>
    <div class="footer-col col-crew">
      <h3>The Gatherly Crew</h3>
      <a href="#">About Us</a>
      <a href="#">Out Story</a>
      <a href="#">Contact Us</a>
    </div>
    <div class="footer-col col-business">
      <h3>Businessy Stuff</h3>
      <a class="strong" href="#">Advertising</a>
    </div>
  </footer>
</body>
</html>
```